Marco Bellin Photography needs a business card designs

I am looking for a business card with a logo clean and simple which I can use that logo on my website or on my pictures. It has to be very classy and very professional. Please look at my website at www.marcobphoto.com for my signature. I'm thinking of something like that for my signature/logo. I'm still working on my website but you get an idea. I'm open to any design but not too busy graphics.

I will be printing the business card from kelvaprint.com.

Surprise me :)

contact me if you have any questions.

-MB
Updates

I'm receiving a lot of black background at the moment. I know my website is all black doesn't mean I want my card to be all black. Please send in with some white background as well. Thanks :)

check out some business cards that I found online. I think they are simple and look really awesome. I don't want a card that is too busy.

http://www.marcobphoto.com/p270092084

Reason: Please extend the date for me. I haven't really receive any good design yet.

Industry/Entity Type

Printing

Requirements
Nice to have
• -a logo that related to my first and last initial of my name "MB"
-double sided
Should not have
• -I don't want my background to be all black.
-no pictures on the card

```html
<!DOCTYPE html>
<html lang="en">
<head>
<meta charset="utf-8">
<title>Marco Bellin Photography – Business Card</title>
<link rel="stylesheet" href="https://fonts.googleapis.com/css2?family=Cinzel:wght@400;600&family=Julius+Sans+One&family=Architects+Daughter&display=swap">
<style>
  :root {
    --page-bg: #141416;
    --front-light: #d9d9d9;
    --front-mid: #a9a9a9;
    --front-dark: #7a7a7a;
    --art-top: #8e8e90;
    --art-bottom: #5c5c5e;
    --back-dark: #0f141b;
    --back-mid: #1d2836;
    --ink-white: #ffffff;
    --ink-soft: #e4e6ea;
    --rule-light: rgba(255,255,255,0.55);
  }
  * { box-sizing: border-box; margin: 0; padding: 0; }
  html, body {
    width: 1200px; height: 871px; overflow: hidden;
    background: var(--page-bg);
  }
  .canvas { position: relative; width: 1200px; height: 871px; }
  .card {
    position: absolute; width: 540px; height: 309px; overflow: hidden;
    border-radius: 3px;
  }

  /* Front side */
  .card-front {
    left: 40px; top: 281px;
    background: linear-gradient(160deg, var(--front-light) 0%, var(--front-mid) 55%, var(--front-dark) 100%);
  }
  .front-art {
    position: absolute; left: 150px; top: 18px; width: 230px; height: 118px;
    background: linear-gradient(180deg, var(--art-top) 0%, var(--art-bottom) 100%);
  }
  .front-rule {
    position: absolute; left: 0; right: 0; height: 1px; background: var(--rule-light);
  }
  .front-rule.upper { top: 186px; }
  .front-rule.lower { top: 268px; }
  .front-brand {
    position: absolute; left: 120px; top: 142px;
    display: flex; align-items: center; gap: 10px;
  }
  .brand-mark { width: 14px; height: 14px; border: 2px solid var(--ink-white); }
  .front-name {
    font-family: "Cinzel", serif; font-weight: 600; font-size: 34px;
    line-height: 40px; letter-spacing: 1px; color: var(--ink-white);
  }
  .front-tagline {
    position: absolute; left: 190px; top: 198px;
    font-family: "Julius Sans One", sans-serif; font-size: 30px; line-height: 36px;
    letter-spacing: 3px; color: var(--ink-white);
  }

  /* Back side */
  .card-back {
    left: 620px; top: 281px;
    background:
      repeating-linear-gradient(90deg, rgba(255,255,255,0.025) 0 1px, rgba(0,0,0,0) 1px 3px),
      linear-gradient(135deg, var(--back-dark) 0%, var(--back-mid) 50%, var(--back-dark) 100%);
  }
  .back-brand {
    position: absolute; left: 26px; top: 26px;
    display: flex; align-items: center; gap: 8px;
  }
  .back-brand .brand-mark { width: 10px; height: 10px; border-width: 1.5px; }
  .back-name {
    font-family: "Cinzel", serif; font-weight: 600; font-size: 18px;
    color: var(--ink-white); letter-spacing: 0.5px;
  }
  .back-signature {
    position: absolute; left: 32px; top: 72px;
    font-family: "Architects Daughter", cursive; font-size: 17px; line-height: 1.1;
    color: var(--ink-soft);
  }
  .contact-list {
    position: absolute; left: 200px; top: 176px;
    display: grid; grid-template-columns: auto 1fr; column-gap: 6px; row-gap: 1px;
    font-family: "Cinzel", serif; font-size: 15px; line-height: 1.15;
    color: var(--ink-white);
  }
  .contact-label::after { content: " :"; }
</style>
</head>
<body>
<main class="canvas">
  <section class="card card-front" aria-label="Card front">
    <div class="front-art" role="img" aria-label="Camera lens artwork area"></div>
    <div class="front-rule upper"></div>
    <div class="front-rule lower"></div>
    <div class="front-brand">
      <span class="brand-mark"></span>
      <span class="front-name">MARCO BELLIN</span>
    </div>
    <div class="front-tagline">PHOTOGRAPHY</div>
  </section>

  <section class="card card-back" aria-label="Card back">
    <div class="back-brand">
      <span class="brand-mark"></span>
      <span class="back-name">MARCO BELLIN</span>
    </div>
    <p class="back-signature">Marco Bellin<br>Photography</p>
    <dl class="contact-list">
      <dt class="contact-label">Adress</dt><dd>Line 1</dd>
      <dt class="contact-label">Phone</dt><dd>501-555-0174</dd>
      <dt class="contact-label">Mobile</dt><dd>501-555-0139</dd>
      <dt class="contact-label">E-mail</dt><dd>marcobellin@studiomail.com</dd>
      <dt class="contact-label">Website</dt><dd>www.marcobphoto.com</dd>
    </dl>
  </section>
</main>
</body>
</html>
```